Psychiatrist/ Psychotherapist needs a letterhead design

I am a Psychiatrist working in private practice. I work as a psychotherapist and treat patients with depression, anxiety, post traumatic stress and relationship problems. I need a letterhead which is elegant and professional. I would like to see designs using colours such as blues and greys.
I would like the information on the letterhead split between the top and bottom of the page to give it a look of balance.
I want it to look elegant, feminine and upmarket. I don't want it to look too corporate but to show some flair and to be a bit artistic.

Target Market(s)

Other doctors, specialists and agencies who have referred patients to me.

Industry/Entity Type

Work

Font styles to use
Script

Requirements
Must have
• My name and my profession psychiatrist need to be highlighted and prominent. It needs to be professional looking and elegant without being old fashioned or too conservative.
Nice to have
• Balance between the top and bottom of the page.
Should not have
• I don't want fonts which are old and too traditional.

```html
<!DOCTYPE html>
<html lang="en">
<head>
<meta charset="utf-8">
<title>Dr. Miriam Calloway – Psychiatrist Letterhead</title>
<link href="https://fonts.googleapis.com/css2?family=Open+Sans:wght@400;600&family=Cormorant+Garamond:wght@500&display=swap" rel="stylesheet">
<style>
  :root {
    --page: #e4e5e9;
    --header-light: #f3f3f6;
    --violet: #7a72b6;
    --violet-deep: #6a62a8;
    --violet-soft: #b4aed8;
    --ink: #4f4f57;
    --white: #ffffff;
  }
  html, body { margin: 0; padding: 0; overflow: hidden; }
  .letterhead {
    position: relative;
    width: 851px;
    height: 1200px;
    background: var(--page);
    overflow: hidden;
    font-family: "Open Sans", Arial, sans-serif;
  }
  .header-wave { position: absolute; left: 0; top: 0; width: 851px; height: 230px; }
  .profile-art {
    position: absolute;
    left: 30px; top: 0;
    width: 100px; height: 168px;
    background: linear-gradient(180deg, var(--violet-soft), var(--violet));
    border-radius: 0 0 40px 30px;
    opacity: .85;
  }
  .header-row {
    position: absolute; left: 156px; top: 22px;
    display: flex; align-items: flex-start;
  }
  .identity { color: var(--ink); white-space: nowrap; }
  .identity .name { margin: 0; font-size: 27px; font-weight: 400; letter-spacing: .2px; line-height: 1.1; }
  .identity .credentials { margin: 6px 0 0; font-size: 15px; line-height: 1; }
  .divider-bar {
    flex: none;
    width: 4px; height: 44px; margin: 4px 24px 0 20px;
    background: var(--violet);
  }
  .profession {
    margin: -8px 0 0;
    font-family: "Cormorant Garamond", Georgia, serif;
    font-weight: 500; font-size: 44px; letter-spacing: 6px; line-height: 1.2;
    color: var(--violet); white-space: nowrap;
  }
  .footer {
    position: absolute; left: 0; bottom: 0;
    width: 851px; height: 72px;
    background: linear-gradient(180deg, var(--violet), var(--violet-deep));
    display: flex; align-items: center; justify-content: space-between;
    padding: 0 22px; box-sizing: border-box;
    color: var(--white); font-size: 12.5px;
  }
  .footer .item { text-align: center; line-height: 1.35; }
  .footer .sep { width: 3px; height: 30px; background: var(--white); }
</style>
</head>
<body>
<div class="letterhead">
  <svg class="header-wave" viewBox="0 0 851 230" aria-hidden="true">
    <path d="M0 0 H851 V125 C700 150 520 190 330 190 C200 190 90 180 0 175 Z" fill="var(--header-light)"/>
    <path d="M0 172 C90 178 200 186 330 186 C520 186 700 148 851 122 L851 132 C700 160 520 198 330 198 C200 198 90 190 0 182 Z" fill="var(--violet)"/>
    <path d="M0 186 C110 194 220 200 340 200 C520 200 700 168 851 140" fill="none" stroke="var(--violet-soft)" stroke-width="2" opacity=".6"/>
  </svg>

  <div class="profile-art" role="img" aria-label="Soft violet silhouette of a head in profile"></div>

  <div class="header-row">
    <div class="identity">
      <p class="name">Dr. Miriam Calloway</p>
      <p class="credentials">B.Med, FRANZCP</p>
    </div>
    <div class="divider-bar"></div>
    <h1 class="profession">Psychiatrist</h1>
  </div>

  <footer class="footer">
    <div class="item">14 Linden Avenue, Norwood, SA 5067</div>
    <div class="sep"></div>
    <div class="item">Tel : (08) 5550 1824, Fax : (08) 5550 1825<br>Mobile : 0400555317</div>
    <div class="sep"></div>
    <div class="item">Email : mcalloway@mindmail.net</div>
  </footer>
</div>
</body>
</html>
```